Company PowerPoint Presentation Template

I am looking for a business powerpoint template tailored to my company that specializes in permafrost services for the mining, transportation, and oil & gas industries. The template would be used to present project findings from studies completed for our clients. I am looking for a crisp, technical, professional business look to the template. Our business is located in North America and English is the primary language used to communicate our work. Complimentary colors associated with the business is blue (RGB, 0,112,192) or something similar in color.

```html
<!DOCTYPE html>
<html lang="en">
<head>
<meta charset="utf-8">
<title>Tundra Ground Consulting – Presentation Template</title>
<link href="https://fonts.googleapis.com/css2?family=Krona+One&family=Lato:wght@400;700&family=Poppins:wght@400;500&display=swap" rel="stylesheet">
<style>
:root{
  --canvas:#8c8c8c;
  --white:#ffffff;
  --blue:#1e2aa0;
  --navy:#111821;
  --ink:#1c1c1c;
  --muted:#555a60;
  --tile:#f4f5f7;
}
*{box-sizing:border-box;margin:0;padding:0}
html,body{width:1200px;height:4231px;overflow:hidden}
body{background:var(--canvas);position:relative;font-family:'Lato',sans-serif;color:var(--ink)}
.slide{position:absolute;left:59px;width:1080px;height:607px;background:var(--white);overflow:hidden}
.abs{position:absolute}
.wordmark{font-family:'Krona One',sans-serif;color:var(--navy);text-transform:uppercase;line-height:1}
.wordmark .sub{display:block;font-family:'Lato',sans-serif;font-weight:400;letter-spacing:.42em}
.slide-title{position:absolute;left:80px;top:58px;font-family:'Krona One',sans-serif;font-size:26px;color:var(--navy)}
.title-rule{position:absolute;left:0;top:95px;width:168px;height:2px;background:var(--blue)}
.corner-mark{position:absolute;left:905px;top:40px;width:141px;text-align:center}
.corner-mark .name{font-size:16px}
.corner-mark .sub{font-size:5px;margin-top:3px;letter-spacing:.38em}

/* cover */
.cover-mark{left:18px;top:265px;width:400px;text-align:center}
.cover-mark .name{font-size:50px;letter-spacing:.02em}
.cover-mark .sub{font-size:15px;margin-top:10px}

/* about */
.about-bg{left:0;top:0;width:1080px;height:607px;background:linear-gradient(160deg,#f6ece4 0%,#f3e6dc 55%,#efe0d4 100%)}
.about-text{left:140px;top:182px;width:800px;text-align:center;font-size:19px;line-height:34px;color:#2b2b2b}
.about-big{left:40px;top:338px;width:1000px;text-align:center;font-family:'Krona One',sans-serif;font-size:96px;color:#b6ac6a;line-height:1}

/* services */
.card{position:absolute;top:187px;width:184px;height:289px;background:var(--white);box-shadow:0 2px 8px rgba(0,0,0,.18);border-radius:3px;overflow:hidden}
.card .photo{height:138px}
.card h3{font-family:'Poppins',sans-serif;font-weight:500;font-size:12.5px;line-height:19px;text-align:center;margin:12px 8px 6px;color:#222}
.card p{font-family:'Poppins',sans-serif;font-size:7.4px;line-height:11.2px;text-align:justify;padding:0 10px;color:#444}

/* projects */
.project{position:absolute;width:300px;height:190px}

/* clients */
.clients-bg{left:0;top:0;width:1080px;height:607px;background:var(--tile)}
.client{position:absolute;width:183px;height:82px;background:var(--white);border-radius:12px;box-shadow:0 2px 6px rgba(0,0,0,.16);display:flex;align-items:center;justify-content:center;gap:8px;font-family:'Lato',sans-serif;font-weight:700;font-size:13px;color:var(--navy)}
.client .dot{width:18px;height:18px;border-radius:50%;background:var(--blue)}

/* thank you */
.thanks-mark{left:639px;top:122px;width:430px;text-align:center}
.thanks-mark .name{font-size:44px}
.thanks-mark .sub{font-size:16px;margin-top:14px}
.thanks{left:639px;top:248px;width:355px;display:flex;align-items:center;gap:12px;font-family:'Krona One',sans-serif;font-size:33px;color:var(--blue)}
.thanks .line{flex:1;height:2px;background:var(--blue)}
.presenter{left:639px;top:330px;font-family:'Poppins',sans-serif;font-size:18px;color:var(--navy)}
.contact{position:absolute;left:639px;display:flex;align-items:flex-start;gap:10px;font-family:'Poppins',sans-serif;font-size:11.5px;line-height:17px;color:#333;width:300px}
.contact svg{flex:none;width:16px;height:16px;fill:var(--navy);margin-top:1px}
</style>
</head>
<body>

<!-- Cover -->
<section class="slide" style="top:84px">
  <svg class="abs" style="left:0;top:0" width="1080" height="607" viewBox="0 0 1080 607">
    <defs>
      <radialGradient id="oilTone" cx="0.78" cy="0.62" r="0.7">
        <stop offset="0" stop-color="#d9a72a"/>
        <stop offset="0.45" stop-color="#7a5a14"/>
        <stop offset="1" stop-color="#231c0c"/>
      </radialGradient>
    </defs>
    <polygon points="499,0 1080,0 1080,607 639,607 573,490 675,305" fill="url(#oilTone)" role="img" aria-label="Photo of a golden oil droplet splashing into a pool of oil"/>
    <polygon points="291,0 499,0 675,305 573,490 470,305" fill="var(--blue)"/>
    <polygon points="470,305 573,490 502,607 394,607" fill="var(--navy)"/>
  </svg>
  <div class="abs wordmark cover-mark"><span class="name">Tundra</span><span class="sub">Ground Consulting</span></div>
</section>

<!-- About -->
<section class="slide" style="top:762px">
  <div class="abs about-bg" role="img" aria-label="Faded photo of an oil pumpjack at sunset"></div>
  <h2 class="slide-title">ABOUT US</h2>
  <div class="title-rule"></div>
  <div class="corner-mark wordmark"><span class="name">Tundra</span><span class="sub">Ground Consulting</span></div>
  <p class="abs about-text">Our core mission is to provide high-quality technical services and practical solutions to solve present-day and future challenges in dynamic permafrost environments vulnerable to climate change</p>
  <div class="abs about-big">TUNDRA</div>
</section>

<!-- Core services -->
<section class="slide" style="top:1448px">
  <h2 class="slide-title">CORE SERVICES</h2>
  <div class="title-rule"></div>
  <div class="corner-mark wordmark"><span class="name">Tundra</span><span class="sub">Ground Consulting</span></div>

  <article class="card" style="left:34px">
    <div class="photo" role="img" aria-label="Photo of an industrial plant at dusk" style="background:linear-gradient(180deg,#3e4a63,#b08a4e)"></div>
    <h3>Thermal Design of Infrastructure</h3>
    <p>Our thermal design services complement civil and geotechnical engineering to deliver high-performance structures in frozen ground, including foundations, roads, pads, pipelines and tanks.</p>
  </article>
  <article class="card" style="left:243px">
    <div class="photo" role="img" aria-label="Photo of engineers in hard hats reviewing a tablet" style="background:linear-gradient(180deg,#9aa3ab,#6f7a5a)"></div>
    <h3>Ground Thermal Analysis and Monitoring</h3>
    <p>Ground thermal analysis relies on accurate temperature measurements. We use modern cables and data loggers to characterize the thermal regime of permafrost.</p>
  </article>
  <article class="card" style="left:452px">
    <div class="photo" role="img" aria-label="Photo of a gloved hand sampling water" style="background:linear-gradient(180deg,#6f8a4c,#3d5230)"></div>
    <h3>Surface and Groundwater Interactions</h3>
    <p>Our team works closely with hydrologists to understand how surface water and groundwater interact at project sites, including thermal erosion and heat transfer.</p>
  </article>
  <article class="card" style="left:661px">
    <div class="photo" role="img" aria-label="Photo of a map with red pins" style="background:linear-gradient(180deg,#d9dbe0,#c8b8a8)"></div>
    <h3>Terrain and Hazard Mapping</h3>
    <p>Our terrain and hazard mapping services focus on local and corridor scale mapping. We produce clear map products for specialists, regulators and the public.</p>
  </article>
  <article class="card" style="left:870px">
    <div class="photo" role="img" aria-label="Photo of engineers at monitoring screens" style="background:linear-gradient(180deg,#2c3a48,#4f6478)"></div>
    <h3>Infrastructure Performance Monitoring</h3>
    <p>We use the latest technology to monitor the performance of infrastructure built on ice-rich soils, reducing risk and cost through timely mitigation measures.</p>
  </article>
</section>

<!-- Recent projects -->
<section class="slide" style="top:2139px">
  <h2 class="slide-title">RECENT PROJECTS</h2>
  <div class="title-rule"></div>
  <div class="corner-mark wordmark"><span class="name">Tundra</span><span class="sub">Ground Consulting</span></div>

  <div class="project" style="left:64px;top:148px;background:linear-gradient(180deg,#8fb0d4,#5c6a78)" role="img" aria-label="Photo of workers in front of a refinery"></div>
  <div class="project" style="left:402px;top:148px;background:linear-gradient(135deg,#c9ccd0,#2f7a68)" role="img" aria-label="Photo of technicians among plant machinery"></div>
  <div class="project" style="left:740px;top:148px;background:linear-gradient(180deg,#4aa0d8,#c9884a)" role="img" aria-label="Photo of solar panels and wind turbines"></div>
  <div class="project" style="left:0;top:373px;width:190px;background:linear-gradient(135deg,#3a3a34,#a89a3a)" role="img" aria-label="Photo of workers in safety gear"></div>
  <div class="project" style="left:228px;top:373px;background:linear-gradient(180deg,#6a6a9a,#c8a6b0)" role="img" aria-label="Photo of a refinery with storage tanks"></div>
  <div class="project" style="left:568px;top:373px;background:linear-gradient(180deg,#6aa6d8,#8a7a68)" role="img" aria-label="Photo of a worker at pipeline valves"></div>
  <div class="project" style="left:906px;top:373px;width:174px;background:linear-gradient(180deg,#7fb0e0,#c6d4e2)" role="img" aria-label="Photo of a refinery tower under blue sky"></div>
</section>

<!-- Clients -->
<section class="slide" style="top:2842px">
  <div class="abs clients-bg"></div>
  <h2 class="slide-title">OUR CLIENTS</h2>
  <div class="title-rule"></div>
  <div class="corner-mark wordmark"><span class="name">Tundra</span><span class="sub">Ground Consulting</span></div>

  <div class="client" style="left:118px;top:175px"><span class="dot"></span>Halden Energy</div>
  <div class="client" style="left:338px;top:175px"><span class="dot"></span>Ember Gas</div>
  <div class="client" style="left:558px;top:175px"><span class="dot"></span>Polar Oil</div>
  <div class="client" style="left:780px;top:175px"><span class="dot"></span>Ridgeway Gas</div>
  <div class="client" style="left:118px;top:282px"><span class="dot"></span>Kestrel Drilling</div>
  <div class="client" style="left:338px;top:282px"><span class="dot"></span>Crestline Fuels</div>
  <div class="client" style="left:558px;top:282px"><span class="dot"></span>Summit Petro</div>
  <div class="client" style="left:780px;top:282px"><span class="dot"></span>Verda Biofuel</div>
  <div class="client" style="left:118px;top:389px"><span class="dot"></span>Lakehead Oil</div>
  <div class="client" style="left:338px;top:389px"><span class="dot"></span>Granite Gas</div>
  <div class="client" style="left:558px;top:389px"><span class="dot"></span>Northpoint Fuel</div>
  <div class="client" style="left:780px;top:389px"><span class="dot"></span>Ironvale Energy</div>
</section>

<!-- Thank you -->
<section class="slide" style="top:3538px">
  <svg class="abs" style="left:0;top:0" width="700" height="607" viewBox="0 0 700 607">
    <defs>
      <linearGradient id="sunsetTone" x1="0" y1="0" x2="0" y2="1">
        <stop offset="0" stop-color="#4d6a8c"/>
        <stop offset="0.45" stop-color="#c9703a"/>
        <stop offset="0.7" stop-color="#f0a040"/>
        <stop offset="1" stop-color="#5a2a18"/>
      </linearGradient>
    </defs>
    <path d="M0,0 H639 C560,60 560,200 470,260 C380,320 380,420 440,480 C500,540 560,560 500,607 H0 Z" fill="url(#sunsetTone)" role="img" aria-label="Photo of refinery pipelines at sunset"/>
  </svg>
  <div class="abs wordmark thanks-mark"><span class="name">Tundra</span><span class="sub">Ground Consulting</span></div>
  <div class="abs thanks"><span class="line"></span>THANK YOU<span class="line"></span></div>
  <div class="abs presenter">PRESENTER NAME</div>

  <div class="contact" style="top:379px"><svg viewBox="0 0 24 24"><path d="M6.6 10.8a15.1 15.1 0 0 0 6.6 6.6l2.2-2.2a1 1 0 0 1 1-.25 11.4 11.4 0 0 0 3.6.57 1 1 0 0 1 1 1V20a1 1 0 0 1-1 1A17 17 0 0 1 3 4a1 1 0 0 1 1-1h3.5a1 1 0 0 1 1 1 11.4 11.4 0 0 0 .57 3.6 1 1 0 0 1-.25 1z"/></svg>(555) 014-2290</div>
  <div class="contact" style="top:418px"><svg viewBox="0 0 24 24"><path d="M12 2a10 10 0 1 0 0 20 10 10 0 0 0 0-20zm6.9 6h-2.9a15.7 15.7 0 0 0-1.4-3.6A8 8 0 0 1 18.9 8zM12 4c.8 1.2 1.5 2.5 1.9 4h-3.8c.4-1.5 1.1-2.8 1.9-4zM4.3 14a8 8 0 0 1 0-4h3.4a16.5 16.5 0 0 0 0 4zm.8 2h2.9a15.7 15.7 0 0 0 1.4 3.6A8 8 0 0 1 5.1 16zM8 8H5.1a8 8 0 0 1 4.3-3.6A15.7 15.7 0 0 0 8 8zm4 12c-.8-1.2-1.5-2.5-1.9-4h3.8c-.4 1.5-1.1 2.8-1.9 4zm2.3-6H9.7a14.7 14.7 0 0 1 0-4h4.6a14.7 14.7 0 0 1 0 4zm.3 5.6A15.7 15.7 0 0 0 16 16h2.9a8 8 0 0 1-4.3 3.6zM16.3 14a16.5 16.5 0 0 0 0-4h3.4a8 8 0 0 1 0 4z"/></svg>www.tundragroundconsulting.com</div>
  <div class="contact" style="top:455px"><svg viewBox="0 0 24 24"><path d="M3 5h18a1 1 0 0 1 1 1v12a1 1 0 0 1-1 1H3a1 1 0 0 1-1-1V6a1 1 0 0 1 1-1zm9 7.5L20 7H4z"/></svg>info@tundragroundconsulting.com</div>
  <div class="contact" style="top:490px"><svg viewBox="0 0 24 24"><path d="M12 2a7 7 0 0 0-7 7c0 5.3 7 13 7 13s7-7.7 7-13a7 7 0 0 0-7-7zm0 9.5A2.5 2.5 0 1 1 12 6.5a2.5 2.5 0 0 1 0 5z"/></svg>123, Lorem ipsum dolor sit amet, consectetur adipiscing elit</div>
</section>

</body>
</html>
```